Pagina Lartécnica

The Lartécnica is a company dealing with leasing and selling real estate. The current site can be accessed at www.lartecnica-exemplo.com.br. We intend to redesign the look of the site and for that we would like to redesign the home page and the page with information and pictures of the property. The homepage should maintain the characteristics of the current common design simple, short and straightforward. The page with the data of the properties should be accessed with two changes page as it is currently running. The search from the map by region and should be maintained.
The page containing the information of the property will provide a total of 15 small pictures that when clicked will appear in larger size. The colors to be used should be orange, blue, black and white. The map can be maintained in the current colors.
Updates

Project Deadline Extended
Reason: Payment guarante!!

Payment guaranteed. Deadline for submission of designs April 27.

Industry/Entity Type

Real Estate

Requirements
Must have
• Search by map regions and search box
address
keep colors from the current page
phones
clean look
Nice to have
• clean look
Should not have
• We like the current page. We just want to make it compatible with modern and new design trends and monitors.

```html
<!DOCTYPE html>
<html lang="en">
<head>
<meta charset="utf-8">
<title>Lartécnica – Home</title>
<link rel="stylesheet" href="https://fonts.googleapis.com/css2?family=Arimo:wght@400;700&display=swap">
<style>
:root{
  --purple:#524c6d;
  --orange:#e8711a;
  --orange-dark:#d9620f;
  --sand:#e9cfad;
  --cream:#fbebd4;
  --cream-edge:#fdf3e5;
  --ink:#2a2a2a;
  --text:#333;
  --brown:#a0642a;
  --yellow-top:#f8cf2a;
  --yellow-bottom:#e3a606;
}
*{margin:0;padding:0;box-sizing:border-box}
html,body{width:1200px;height:1146px;overflow:hidden;background:#fff}
body{font-family:"Arimo",Arial,sans-serif;color:var(--text);position:relative}
.abs{position:absolute}

.top-bar,.bottom-bar{position:absolute;left:0;width:1200px;height:8px;background:var(--purple)}
.top-bar{top:0}.bottom-bar{top:1136px;height:10px}

.brand{left:212px;top:40px;display:flex;align-items:center;gap:10px}
.brand-mark{width:26px;height:26px;background:var(--orange)}
.brand-name{font-size:34px;font-weight:700;color:var(--purple);letter-spacing:-.5px}

.sale-phone{right:220px;top:20px;font-size:18px;font-weight:700;color:#000}
.sale-phone span{color:var(--orange);font-weight:400}

.main-nav{left:590px;top:58px;display:flex;gap:16px;font-size:10px;font-weight:700;color:var(--ink);letter-spacing:.2px}
.main-nav .caret{font-size:8px}

.hero-band{left:0;top:106px;width:1200px;height:330px;background:var(--sand)}
.hero-photo{left:198px;top:107px;width:800px;height:318px;background:linear-gradient(120deg,#c9a46a 0%,#e8dcc2 35%,#9a5a34 60%,#d9d3c2 80%,#7d9c5c 100%)}
.hero-caption{left:198px;top:391px;width:800px;height:30px;background:var(--orange-dark);color:#fff;font-size:14px;font-weight:700;padding:7px 0 0 26px;letter-spacing:.2px}
.hero-dots{position:absolute;right:12px;top:12px;display:flex;gap:3px}
.hero-dots i{width:9px;height:7px;background:#f6cfae;display:block}

.search-panel{left:198px;top:438px;width:800px;height:207px;background:var(--cream)}
.search-title{left:212px;top:448px;font-size:11.5px;font-weight:700;color:var(--ink)}
.search-intro,.search-note{font-size:9.6px;line-height:14.4px;color:var(--text);width:610px}
.search-intro{left:213px;top:463px}
.search-note{left:216px;top:595px}
.field{background:#fff;border:1px solid #d5cbbd;height:28px;font-size:10px;color:#333;padding:8px 0 0 11px}
.field-location{left:214px;top:502px;width:223px}
.field-region{left:479px;top:502px;width:223px}
.field svg{position:absolute;right:8px;top:7px}
.or{left:449px;top:512px;font-size:10px}
.search-btn{left:215px;top:542px;width:112px;height:32px;border:1px solid #c98f05;border-radius:3px;background:linear-gradient(var(--yellow-top),var(--yellow-bottom));color:#fff;font-size:14px;text-align:center;padding-top:8px;letter-spacing:.3px}
.region-map{left:852px;top:450px;width:127px;height:155px;background:linear-gradient(140deg,#6aa3d8,#f3e3a2 55%,#5f9dd6)}
.map-caption{left:843px;top:613px;font-size:7px;color:var(--ink);letter-spacing:.2px}

.card{top:671px;width:219px;height:276px;background:var(--cream-edge)}
.card-inner{position:absolute;left:9px;top:7px;width:202px;height:261px;background:var(--cream)}
.card-photo{position:absolute;left:8px;top:7px;width:188px;height:125px}
.card h3{position:absolute;font-size:11.5px;font-weight:700;color:var(--ink);letter-spacing:.3px}
.card p{position:absolute;font-size:9.6px;line-height:14.4px;color:var(--text)}
.card .more{position:absolute;font-size:10px;font-weight:700;color:var(--ink)}

.footer{left:0;top:993px;width:1200px;height:143px;background:var(--sand)}
.footer-nav{left:220px;top:1033px;display:flex;gap:16px;font-size:10px;font-weight:700;color:var(--ink)}
.legal{left:220px;top:1057px;font-size:10px;line-height:11.5px;color:var(--brown)}
.social{left:880px;top:1014px;display:flex;gap:8px}
.social i{width:16px;height:16px;border-radius:50%;background:#4a3d36;display:block}
</style>
</head>
<body>
<div class="top-bar"></div>

<header>
  <div class="abs brand"><span class="brand-mark"></span><span class="brand-name">Lartécnica</span></div>
  <div class="abs sale-phone">For sale: <span>(48) 5550-0147</span></div>
  <nav class="abs main-nav">
    <span>HOME</span><span>COMPANY</span><span>LOCATION</span><span>REGISTER</span><span>INFORMATION <span class="caret">▼</span></span><span>CONTACT US</span>
  </nav>
</header>

<section>
  <div class="abs hero-band"></div>
  <div class="abs hero-photo" role="img" aria-label="Photo of a bright kitchen with island, wooden floor and windows"></div>
  <div class="abs hero-caption">PERSONALIZED SEARCH SERVICE FOR YOUR REAL ESTATE NEEDS
    <div class="hero-dots"><i></i><i></i><i></i><i></i><i></i></div>
  </div>
</section>

<section>
  <div class="abs search-panel"></div>
  <div class="abs search-title">SEARCH PROPERTY BY REGION (LEASE)</div>
  <p class="abs search-intro">Lorem ipsum dolor sit amet, consectetur adipisicing elit, sed do eiusmod tempor incididunt ut labore et dolore magna aliqua. Ut enim ad minim veniam, quis nostrud exercitation ullamco laboris nisi ut aliquip ex ea commodo consequat.</p>
  <div class="abs field field-location">Enter your location
    <svg width="14" height="14" viewBox="0 0 14 14"><circle cx="5.5" cy="5.5" r="4.3" fill="none" stroke="#aaa" stroke-width="1.5"/><line x1="8.6" y1="8.6" x2="13" y2="13" stroke="#aaa" stroke-width="2"/></svg>
  </div>
  <div class="abs or">Or</div>
  <div class="abs field field-region">Choose your region
    <svg width="9" height="8" viewBox="0 0 9 8" style="top:10px"><path d="M0 0h9L4.5 8z" fill="#111"/></svg>
  </div>
  <div class="abs search-btn">SEARCH</div>
  <p class="abs search-note">Lorem ipsum dolor sit amet, consectetur adipisicing elit, sed do eiusmod tempor incididunt ut labore et dolore magna aliqua. Ut enim ad minim veniam, quis nostrud exercitation ullamco laboris nisi ut aliquip ex ea commodo consequat.</p>
  <div class="abs region-map" role="img" aria-label="Regional map of the island and coastline"></div>
  <div class="abs map-caption">SEARCH PROPERTY BY REGION (LEASE)</div>
</section>

<section>
  <article class="abs card" style="left:239px">
    <div class="card-inner">
      <h3 style="left:12px;top:14px">ABOUT OUR COMPANY</h3>
      <p style="left:14px;top:54px;width:182px">The Lartécnica, for more than fifteen years in the real estate market, permeated with values and culture defined by the needs of its clients, has been gradually building a solid body for the management and sale of real estate. These years marked by moments of achievement and adversity, brought him the wisdom necessary to build step by step a big difference in the provision of its services.</p>
      <span class="more" style="left:16px;top:236px">READ MORE..</span>
    </div>
  </article>
  <article class="abs card" style="left:488px">
    <div class="card-inner">
      <div class="card-photo" style="background:linear-gradient(160deg,#8fb06a,#d8d6cf 50%,#8a6a52)" role="img" aria-label="Photo of a modern two-storey house"></div>
      <h3 style="left:13px;top:140px">REAL ESTATE LISTING</h3>
      <p style="left:14px;top:160px;width:188px">Lorem ipsum dolor sit amet, consectetur adipisicing elit, sed do eiusmod tempor incididunt ut labore et dolore magna aliqua. Ut enim ad minim</p>
      <span class="more" style="left:14px;top:227px">READ MORE..</span>
    </div>
  </article>
  <article class="abs card" style="left:737px">
    <div class="card-inner">
      <div class="card-photo" style="left:10px;width:186px;background:linear-gradient(180deg,#d8dde3,#7c6a5c 55%,#6f8f4e)" role="img" aria-label="Photo of a suburban stone family house"></div>
      <h3 style="left:12px;top:140px">REAL ESTATE LISTING</h3>
      <p style="left:12px;top:160px;width:188px">Lorem ipsum dolor sit amet, consectetur adipisicing elit, sed do eiusmod tempor incididunt ut labore et dolore magna aliqua. Ut enim ad minim</p>
      <span class="more" style="left:14px;top:227px">READ MORE..</span>
    </div>
  </article>
</section>

<footer>
  <div class="abs footer"></div>
  <nav class="abs footer-nav"><span>HOME</span><span>COMPANY</span><span>LOCATION</span><span>REGISTER</span><span>INFORMATION</span><span>CONTACT US</span></nav>
  <div class="abs legal">COPYRIGHT 2013. ALL RIGHTS RESERVED.<br>TERMS &amp; CONDITIONS &nbsp;- &nbsp;PRIVACY &nbsp;- &nbsp;DISCLAIMER</div>
  <div class="abs social"><i></i><i></i><i></i><i></i></div>
</footer>

<div class="bottom-bar"></div>
</body>
</html>
```